create a webpage for optometry practice

I'm looking to create a professional and elegant webpage for my practice. I prefer neutral earthy colors, but I am open to other ideas. I have included an image of my logo to be used in the process. This will be a page that will illustrate information about my practice and the kind of services we offer. I am in process of having the practice remodeled. So I don't have any photos of my practice to include yet.

Target Market(s)

My practice serves young and mature families.

Industry/Entity Type

It Professional

Number of Pages Required

5+ page

Font styles to use
Sans Serif

Colors
33a6d7
86cfc6
85cae6
cadf82
3276b5
faa54b
abd036
f78c1e

Requirements
Must have
• I would need to incorporate information about my practice, services, insurance accepted, make appointment, contact us, and about our family.
Nice to have
• I would like to see something fresh, modern, and unique

```html
<!DOCTYPE html>
<html lang="en">
<head>
<meta charset="utf-8">
<title>Clarion Eye – Optometry Practice</title>
<link rel="stylesheet" href="https://fonts.googleapis.com/css2?family=Open+Sans:wght@300;400;600;700&display=swap">
<style>
:root{
  --teal:#3cb0bd;
  --teal-light:#cdeef3;
  --orange:#f7a04a;
  --orange-deep:#f78c1e;
  --blue:#3276b5;
  --blue-btn:#3561ad;
  --green:#6b9a1c;
  --green-sea:#23a08f;
  --lime:#8cc63f;
  --lime-soft:#c9e3a2;
  --service-blue:#3f69b8;
  --navy:#2f3a6b;
  --navy-line:#48558a;
  --text:#333;
  --muted:#555;
  --gold:#e7cf4c;
}
*{margin:0;padding:0;box-sizing:border-box}
html,body{width:1200px;height:900px;overflow:hidden;background:#fff;font-family:"Open Sans",Arial,sans-serif;color:var(--text)}
.page{position:absolute;left:362px;top:0;width:476px;height:900px;background:#fff}
.abs{position:absolute}

/* header */
.header{left:0;top:0;width:476px;height:44px}
.header svg{position:absolute;left:0;top:0}
.brand{left:12px;top:12px;display:flex;align-items:center;gap:4px;font-size:11px;font-weight:600;color:#35506a;letter-spacing:.2px}
.brand .dot{width:9px;height:9px;border-radius:50%;background:var(--orange-deep)}
.nav{left:223px;top:10px;display:flex;gap:0;font-size:4.6px;color:#fff;text-transform:uppercase}
.nav span{padding:0 4px;line-height:20px}
.nav .active{background:var(--orange-deep)}
.call{right:64px;top:26px;font-size:10.5px;font-weight:700;color:#fff}

/* hero */
.hero{left:0;top:44px;width:476px;height:200px;background:linear-gradient(90deg,#cdd6de 0%,#e6ebef 40%,#d9dfe3 62%,#c7ced4 100%)}
.hero-title{left:65px;top:30px;font-size:20px;font-weight:300;color:#fff;line-height:22px}
.hero-sub{left:65px;top:77px;font-size:8.5px;color:#fff;line-height:11px;width:170px}
.hero-btn{left:65px;top:106px;width:65px;height:14px;background:var(--blue-btn);color:#fff;font-size:5px;line-height:14px;text-align:center}
.dots{left:58px;top:152px;display:flex;gap:1px}
.dots span{width:15px;height:3px;background:#d5d9dc}
.dots span:first-child{background:var(--orange)}

/* features */
.features{left:53px;top:205px;width:370px;height:195px;background:#fff;box-shadow:0 0 12px rgba(0,0,0,.15)}
.card{position:absolute;top:2px;width:80px;text-align:center}
.card .blob{width:67px;height:80px;margin:0 auto;border-radius:8px 8px 26px 26px;display:flex;align-items:center;justify-content:center}
.card h3{font-size:7.8px;font-weight:400;margin-top:9px}
.card p{font-size:4.4px;line-height:8.4px;color:var(--text);margin-top:5px;padding:0 3px}
.card .more{margin-top:8px;font-size:3.8px;color:var(--green-sea);text-transform:uppercase}
.card .more i{display:block;width:5px;height:5px;border:1px solid var(--green-sea);border-radius:50%;margin:0 auto 3px}

/* appointment */
.appoint{left:0;top:403px;width:476px;height:110px;background:linear-gradient(120deg,var(--lime) 0%,#a9d468 45%,var(--lime-soft) 100%)}
.appoint h2{position:absolute;top:9px;width:100%;text-align:center;font-size:12.5px;font-weight:400;color:#222}
.field{position:absolute;width:171px;height:18px;background:#fff;font-size:5px;color:#999;text-align:center;line-height:18px}
.submit{left:204px;top:84px;width:68px;height:18px;border:1px solid #4a6a1a;background:#c8e07c;font-size:6.5px;text-align:center;line-height:16px;color:#223}

/* exam */
.exam-title{left:0;top:529px;width:476px;text-align:center;font-size:13px;font-weight:400;color:#222}
.step{position:absolute;top:565px;display:flex;gap:8px;width:115px}
.step b{flex:none;width:18px;height:18px;border-radius:50%;background:#1f97a0;color:#fff;font-size:7.5px;line-height:18px;text-align:center}
.step p{font-size:4.3px;line-height:7.5px;color:var(--muted)}

/* services */
.services{left:0;top:617px;width:476px;height:123px;background:linear-gradient(90deg,#5379c2 0%,var(--service-blue) 50%,#4d74bd 100%)}
.services h2{position:absolute;top:17px;width:100%;text-align:center;font-size:12px;font-weight:300;color:#fff}
.svc-list{position:absolute;top:45px;font-size:4.3px;line-height:9.7px;color:#fff}
.svc-left{right:243px;text-align:right}
.svc-right{left:243px}

/* footer */
.footer{left:0;top:740px;width:476px;height:160px;background:var(--navy)}
.footer .rule{position:absolute;left:0;width:476px;height:1px;background:var(--navy-line)}
.foot-nav{position:absolute;top:37px;width:100%;display:flex;justify-content:center;gap:8px;font-size:4.4px;color:#fff}
.col{position:absolute;top:56px;text-align:center;color:#fff}
.col h4{font-size:4.8px;font-weight:700;color:var(--gold);margin-bottom:4px}
.col p{font-size:4px;letter-spacing:.5px}
.hours{position:absolute;top:88px;width:100%;text-align:center}
.hours h4{font-size:4.8px;color:var(--gold);margin-bottom:4px}
.hours p{font-size:3.7px;color:#fff}
.hours em{font-style:normal;color:var(--gold)}
.follow{position:absolute;top:119px;width:100%;text-align:center}
.follow h4{font-size:4.8px;color:var(--gold)}
.socials{display:flex;justify-content:center;gap:5px;margin-top:5px}
.socials span{width:10px;height:10px;border-radius:50%;border:1px solid #aab}
.copy{position:absolute;top:151px;width:100%;text-align:center;font-size:3.6px;color:#ccd}
.foot-brand{left:222px;top:5px;display:flex;align-items:center;gap:2px;font-size:5px;font-weight:600;color:#35506a}
.foot-brand .dot{width:4px;height:4px;border-radius:50%;background:var(--orange-deep)}
</style>
</head>
<body>
<div class="page">

  <header class="abs header">
    <svg width="476" height="44" viewBox="0 0 476 44">
      <rect width="476" height="44" fill="var(--teal-light)"/>
      <polygon points="140,0 476,0 476,44 185,44" fill="var(--teal)"/>
    </svg>
    <div class="abs brand"><span class="dot"></span>Clarion Eye</div>
    <nav class="abs nav">
      <span class="active">Home</span><span>About Us</span><span>Treatments</span><span>FAQ</span><span>Our Services</span><span>Lenses</span><span>Contact Us</span>
    </nav>
    <div class="abs call">CALL US: 0100-555-0142</div>
  </header>

  <section class="abs hero" role="img" aria-label="Photo of a smiling woman wearing glasses, resting her chin on her hand, in a bright office">
    <h1 class="abs hero-title">An eye<br>on the future</h1>
    <p class="abs hero-sub">Make an appointment today. Your future suddenly became a whole lot clearer.</p>
    <div class="abs hero-btn">Request Appointment &#9662;</div>
    <div class="abs dots"><span></span><span></span><span></span></div>
  </section>

  <section class="abs features">
    <div class="card" style="left:8px">
      <div class="blob" style="background:var(--orange)">
        <svg width="40" height="40" viewBox="0 0 40 40"><circle cx="20" cy="20" r="17" fill="none" stroke="#fff" stroke-width="1"/><circle cx="20" cy="20" r="11" fill="#fff"/><circle cx="20" cy="14.5" r="1.6" fill="var(--orange)"/><rect x="18.6" y="17.5" width="2.8" height="9" fill="var(--orange)"/></svg>
      </div>
      <h3 style="color:var(--orange)">About</h3>
      <p>We are a local practice built on trust, care and clear advice. Meet the team who will look after your eyes for years to come.</p>
      <div class="more"><i></i>Read more</div>
    </div>
    <div class="card" style="left:105px">
      <div class="blob" style="background:var(--blue)">
        <svg width="40" height="40" viewBox="0 0 40 40"><circle cx="20" cy="20" r="17" fill="none" stroke="#fff" stroke-width="1"/><path d="M11 20 L20 12 L29 20 M13.5 18 V28 H26.5 V18" fill="none" stroke="#fff" stroke-width="1.3"/><path d="M20 26 l-3.2-3.2 a1.8 1.8 0 0 1 3.2-2.3 a1.8 1.8 0 0 1 3.2 2.3z" fill="none" stroke="#fff" stroke-width="1"/></svg>
      </div>
      <h3 style="color:var(--blue)">Our Family</h3>
      <p>From a child's first exam to care for older eyes, we welcome every member of your family with patience and a warm smile.</p>
      <div class="more"><i></i>Read more</div>
    </div>
    <div class="card" style="left:198px">
      <div class="blob" style="background:var(--green)">
        <svg width="40" height="40" viewBox="0 0 40 40"><circle cx="20" cy="20" r="17" fill="none" stroke="#fff" stroke-width="1"/><path d="M6 20 Q20 8 34 20 Q20 32 6 20z" fill="#fff"/><circle cx="20" cy="20" r="5.5" fill="var(--green)"/><circle cx="20" cy="20" r="2.5" fill="#fff"/></svg>
      </div>
      <h3 style="color:var(--green)">Services</h3>
      <p>Full eye exams, contact lens fittings, glasses, eye injury care and checks for glaucoma, all done with modern tools in one place.</p>
      <div class="more"><i></i>Read more</div>
    </div>
    <div class="card" style="left:290px">
      <div class="blob" style="background:var(--green-sea)">
        <svg width="40" height="40" viewBox="0 0 40 40"><circle cx="20" cy="20" r="17" fill="none" stroke="#fff" stroke-width="1"/><path d="M14 10 H23 L27 14 V30 H14z" fill="#fff"/><path d="M16.5 16 H24.5 M16.5 19 H24.5 M16.5 22 H24.5 M16.5 25 H24.5" stroke="var(--green-sea)" stroke-width="1"/></svg>
      </div>
      <h3 style="color:var(--green-sea)">Insurance</h3>
      <p>We accept most vision and health plans. Bring your card to your visit and our staff will help you make sense of your cover.</p>
      <div class="more"><i></i>Read more</div>
    </div>
  </section>

  <section class="abs appoint">
    <h2>Make an Appointment</h2>
    <div class="field" style="left:64px;top:34px">--FIRST NAME--</div>
    <div class="field" style="left:240px;top:34px">--LAST NAME--</div>
    <div class="field" style="left:64px;top:56px">--EMAIL--</div>
    <div class="field" style="left:240px;top:56px">--PHONE NO--</div>
    <div class="abs submit">SUBMIT</div>
  </section>

  <h2 class="abs exam-title">Providing Most Comprehensive Exam Around!</h2>
  <div class="step" style="left:64px"><b>1</b><p>We test how well you see up close and far away, then check eye pressure and health.</p></div>
  <div class="step" style="left:187px"><b>2</b><p>Our doctor looks at the back of the eye with modern imaging to spot problems early.</p></div>
  <div class="step" style="left:309px"><b>3</b><p>You get a clear report, a new prescription if needed and advice for the years ahead.</p></div>

  <section class="abs services" role="img" aria-label="Faded photo of an optometrist examining a patient beside eye testing equipment, tinted blue">
    <h2>Optometry Services Offered</h2>
    <div class="svc-list svc-left">Comprehensive Eye Exams (Adults and Children)<br>Strabismus and Lazy Eye<br>Hard to Fit Contact Lenses<br>Lasik pre-surgical evaluations and post surgical follow up care<br>Cataract pre-surgical evaluations and post-surgical care<br>Glaucoma</div>
    <div class="svc-list svc-right">Contact Lens Fitting and follow up evaluations/Macular Degeneration<br>Eye Injuries<br>Eye Infections<br>Eye Glasses<br>Safety Glasses<br>Sunglasses ( both prescription and non-prescription)</div>
  </section>

  <footer class="abs footer">
    <svg class="abs" style="left:200px;top:0" width="76" height="30" viewBox="0 0 76 30"><polygon points="0,0 76,0 38,30" fill="#fff"/></svg>
    <div class="abs foot-brand"><span class="dot"></span>Clarion Eye</div>
    <nav class="foot-nav"><span>HOME</span><span>ABOUT US</span><span>TREATMENTS</span><span>FAQ</span><span>OUR SERVICES</span><span>LENSES</span><span>CONTACT US</span></nav>
    <div class="rule" style="top:50px"></div>
    <div class="col" style="left:0;width:139px"><h4>CALL US</h4><p>0100-555-0142</p></div>
    <div class="abs" style="left:139px;top:50px;width:1px;height:30px;background:var(--navy-line)"></div>
    <div class="col" style="left:139px;width:170px"><h4>OUR CLINIC</h4><p style="letter-spacing:0">CLARION EYE - 12 BIRCHWOOD LANE, HALEFORD HF2 7QL</p></div>
    <div class="abs" style="left:308px;top:50px;width:1px;height:30px;background:var(--navy-line)"></div>
    <div class="col" style="left:308px;width:168px"><h4>E MAIL</h4><p>hello@clarioneye.example</p></div>
    <div class="rule" style="top:80px"></div>
    <div class="hours"><h4>BUSINESS HOURS</h4><p><em>Monday</em> 8:00am-6:00pm | <em>Tuesday</em> 8:00am-6:00pm | <em>Wednesday</em> 8:00am-6:00pm | <em>Thursday</em> 8:00am-6:00pm | <em>Friday</em> 8:00am-6:00pm | <em>Saturday</em> 9:00am-12:00pm | <em>Sunday</em> Closed</p></div>
    <div class="rule" style="top:113px"></div>
    <div class="follow"><h4>FOLLOW US:</h4><div class="socials"><span></span><span></span><span></span></div></div>
    <div class="rule" style="top:147px"></div>
    <div class="copy">© 2015 All Rights Reserved</div>
  </footer>

</div>
</body>
</html>
```